Flu 2019

Lockridge Regional Hospital is hosting a health fair/flu shot clinic this Fall. What she'd like to convey is the following:

Health Fair & Flu Clinic 2019
At the following locations from 10am - 1pm
Flint Ridge - September 25 at Courthouse in Flint Ridge
Harlow - October 2 at Harlow Multipurpose Center
Tasker - October 9 at Tasker Community Center
No cost flu shots available. Please bring insurance information.
Door prizes - Giveaways - Treats
Brought to you by Lockridge Regional Hospital

We would like to highlight the health fair which will be free to the community. We would like to also highlight the flu clinic; however, the no cost/bring insurance needs to be in smaller print.

```html
<!DOCTYPE html>
<html lang="en">
<head>
<meta charset="utf-8">
<title>Health Fair &amp; Flu Clinic 2019</title>
<link href="https://fonts.googleapis.com/css2?family=Anton&family=Bebas+Neue&family=Montserrat:wght@300;400;600;700&display=swap" rel="stylesheet">
<style>
  :root {
    --page: #ffffff;
    --paper-light: #f3e9e2;
    --paper-mid: #eadbcd;
    --paper-edge: #d8c3ae;
    --ink: #0a0a0a;
    --grey: #7a7a7a;
    --soft-grey: #8a8684;
    --white: #ffffff;
  }
  * { margin: 0; padding: 0; box-sizing: border-box; }
  html, body { width: 964px; height: 1200px; overflow: hidden; background: var(--page); }
  .canvas { position: relative; width: 964px; height: 1200px; }
  .poster {
    position: absolute; left: 105px; top: 63px; width: 768px; height: 1082px;
    background:
      radial-gradient(ellipse at 45% 30%, var(--paper-light) 0%, var(--paper-mid) 65%, var(--paper-edge) 100%);
    overflow: hidden;
  }
  .poster > * { position: absolute; }
  .brand {
    left: 0; width: 100%; top: 52px; text-align: center;
    font-family: "Montserrat", sans-serif; font-weight: 700; font-size: 30px;
    line-height: 38px; color: var(--ink); letter-spacing: 1px;
  }
  .headline {
    left: 0; width: 100%; text-align: center; white-space: nowrap;
    font-family: "Bebas Neue", sans-serif; color: var(--ink); line-height: 1;
  }
  .headline-top { top: 206px; font-size: 118px; }
  .headline-bottom { top: 305px; font-size: 116px; letter-spacing: 1px; }
  .rule { left: 66px; top: 418px; width: 636px; height: 2px; background: var(--ink); }
  .intro-lead {
    left: 36px; top: 432px; font-family: "Anton", sans-serif; font-size: 47px;
    color: var(--grey); line-height: 1; white-space: nowrap;
  }
  .intro-line {
    left: 38px; font-family: "Bebas Neue", sans-serif; font-size: 52px;
    color: var(--ink); line-height: 1; white-space: nowrap;
  }
  .intro-where { top: 500px; }
  .intro-time { top: 558px; }
  .offer {
    left: 0; top: 623px; width: 428px; height: 240px; background: var(--ink);
    color: var(--white); text-align: center;
  }
  .offer-title {
    display: block; margin-top: 40px; font-family: "Anton", sans-serif;
    font-size: 44px; line-height: 1; white-space: nowrap;
  }
  .offer-sub {
    display: block; margin-top: 8px; font-family: "Montserrat", sans-serif;
    font-weight: 300; font-size: 62px; line-height: 1;
  }
  .offer-note {
    display: block; margin-top: 22px; font-family: "Montserrat", sans-serif;
    font-weight: 700; font-size: 15.5px; line-height: 23px; letter-spacing: .3px;
  }
  .extras {
    left: 40px; top: 892px; width: 390px; text-align: center; white-space: nowrap;
    font-family: "Bebas Neue", sans-serif; font-size: 33px; color: var(--ink); line-height: 1;
  }
  .stop { left: 454px; width: 280px; }
  .stop-town {
    display: block; font-family: "Anton", sans-serif; font-size: 35px;
    color: var(--grey); line-height: 1; white-space: nowrap;
  }
  .stop-date {
    display: block; margin-top: 8px; font-family: "Montserrat", sans-serif;
    font-weight: 700; font-size: 28px; color: var(--ink); line-height: 1;
  }
  .stop-venue {
    display: block; margin-top: 12px; font-family: "Montserrat", sans-serif;
    font-weight: 400; font-size: 17px; color: var(--soft-grey); line-height: 38px;
    letter-spacing: .3px; white-space: nowrap;
  }
  .stop-divider { display: block; margin-top: 4px; width: 216px; height: 4px; }
  .stop-1 { top: 436px; }
  .stop-2 { top: 618px; }
  .stop-3 { top: 796px; }
  .footer {
    left: 0; top: 972px; width: 100%; height: 110px; background: var(--ink);
    color: var(--white); text-align: center; padding-top: 12px; white-space: nowrap;
    font-family: "Montserrat", sans-serif; font-weight: 300; font-size: 27px;
    line-height: 39px; letter-spacing: 1px;
  }
</style>
</head>
<body>
<div class="canvas">
  <div class="poster">
    <div class="brand">LOCKRIDGE<br>REGIONAL<br>HOSPITAL</div>

    <h1 class="headline headline-top">HEALTH FAIR &amp;</h1>
    <h1 class="headline headline-bottom">FLU CLINIC 2019</h1>
    <div class="rule"></div>

    <div class="intro-lead">AT THE FOLLOWING</div>
    <div class="intro-line intro-where">LOCATIONS FROM</div>
    <div class="intro-line intro-time">10AM - 1PM</div>

    <div class="offer">
      <span class="offer-title">NO COST FLU SHOTS</span>
      <span class="offer-sub">AVAILABLE</span>
      <span class="offer-note">PLEASE BRING<br>INSURANCE INFORMATION.</span>
    </div>

    <div class="extras">DOOR PRIZES - GIVEAWAYS - TREATS</div>

    <div class="stop stop-1">
      <span class="stop-town">FLINT RIDGE</span>
      <span class="stop-date">SEP- 25</span>
      <span class="stop-venue">AT COURTHOUSE IN<br>FLINT RIDGE</span>
      <svg class="stop-divider" viewBox="0 0 216 4"><line x1="2" y1="2" x2="216" y2="2" stroke="#0a0a0a" stroke-width="2.4" stroke-dasharray="0.1 5" stroke-linecap="round"/></svg>
    </div>

    <div class="stop stop-2">
      <span class="stop-town">HARLOW</span>
      <span class="stop-date">OCT- 2</span>
      <span class="stop-venue">AT HARLOW MULTIPUR<br>POSE CENTER</span>
      <svg class="stop-divider" viewBox="0 0 216 4"><line x1="2" y1="2" x2="216" y2="2" stroke="#0a0a0a" stroke-width="2.4" stroke-dasharray="0.1 5" stroke-linecap="round"/></svg>
    </div>

    <div class="stop stop-3">
      <span class="stop-town">TASKER</span>
      <span class="stop-date">OCT -9</span>
      <span class="stop-venue">AT TASKER COMM<br>UNITY CENTER</span>
      <svg class="stop-divider" viewBox="0 0 216 4"><line x1="2" y1="2" x2="216" y2="2" stroke="#0a0a0a" stroke-width="2.4" stroke-dasharray="0.1 5" stroke-linecap="round"/></svg>
    </div>

    <div class="footer">BROUGHT TO YOU<br>BY LOCKRIDGE REGIONAL HOSPITAL</div>
  </div>
</div>
</body>
</html>
```